New Internet Service provider for regional or isolated businesses

I'm looking for a logo and basic information website for an Internet company - "Quill Harbor Internet". This new company will be providing specialised Internet connectivity for isolated areas or where connectivity is too expensive for one business.
i.e Bringing Businesses together for better more affordable Internet.
3 Types of Pages
1. Home Page
2. Content Page templates
3. More Information Form
1. Contact Name. 2. Business Address. 3. Business Phone Number. 4. Mobile Phone. 5. Number of Staff 6. Current Internet connection . 7. Speed 8. Comments ?
Web Pages
**Quill Harbor Internet **
Bringing Businesses together for better Internet
Who is Quill Harbor Internet ?
How do we work ?
Which carriers ?
Technologies Used ?
Contact details
Check my address now ?
(Form)
Our company will be using Fibre and Microwave/Radio technology to connect remote businesses to high speed Internet
Target Market(s)
Business customers with minimum 10 staff outside metropolitan areas
Industry/Entity Type
Internet Service Provider
Coding
Coded - Design and coding required
Number of Pages Required
3 page
Requirements
Must have
- 3 Types of Pages
- 1. Home Page
- 2. Content Page templates (See above)
- 3. "More Information" Form
- 1. Contact Name. 2. Business Address. 3. Business Phone Number. 4. Mobile Phone. 5. Number of Staff 6.Current Internet connection . 7. Speed 8.Comments ?
Nice to have
- Pictures of fibre optics, radio towers, stock photos of businesses / PC's
- Some ideas on the companies we will be using (I am looking for something similar in my website).
- In order of preference
- 1. www.pelmara.com.au
- 2. www.drusket.com,au
- 3.www.tolvent.com.au

```html
<!DOCTYPE html>
<html lang="en">
<head>
<meta charset="utf-8">
<title>Quill Harbor Internet</title>
<link rel="stylesheet" href="https://fonts.googleapis.com/css2?family=Cinzel:wght@400;700&family=Lato:wght@400;700&display=swap">
<style>
:root{
  --blue:#3d9ad1;
  --blue-dark:#2a7fb4;
  --ink:#1c1c1c;
  --text:#333;
  --light:#eeeeee;
  --band:#6d6d6d;
  --footer:#2a2a2a;
  --footer-text:#c9c9c9;
  --white:#fff;
}
*{box-sizing:border-box;margin:0;padding:0}
html,body{width:727px;height:1200px;overflow:hidden;background:var(--white)}
body{position:relative;font-family:'Lato',sans-serif;color:var(--text)}
.abs{position:absolute}

/* header */
.header{left:0;top:0;width:727px;height:58px;background:var(--white);box-shadow:0 1px 3px rgba(0,0,0,.12);z-index:2}
.header .topline{left:0;top:0;width:727px;height:2px;background:var(--blue)}
.brand{left:48px;top:8px;display:flex;align-items:center;gap:10px}
.brand .mark{width:32px;height:32px;border-radius:50%;border:3px solid var(--blue)}
.brand .name{font-family:'Cinzel',serif;font-size:16px;line-height:17px;color:var(--blue-dark);font-weight:400}
.phone{left:443px;top:4px;font-size:11.5px;font-weight:700;color:var(--ink);display:flex;align-items:center;gap:5px}
.mail-tab{left:544px;top:0;width:146px;height:18px;background:var(--blue);border-radius:0 0 12px 12px;color:var(--white);font-size:8.5px;font-weight:700;display:flex;align-items:center;justify-content:center;gap:5px}
.nav{left:259px;top:36px;display:flex;font-family:'Cinzel',serif;font-size:8.5px;letter-spacing:.6px;color:var(--ink);text-transform:uppercase}
.nav a{color:inherit;text-decoration:none;padding:0 17px;border-left:1px solid #ccc}
.nav a:first-child{border-left:none;color:var(--blue)}

/* hero */
.hero{left:0;top:58px;width:727px;height:291px;
  background:
    radial-gradient(ellipse 170px 130px at 520px 90px,rgba(150,205,245,.85) 0%,rgba(70,150,215,.45) 45%,rgba(0,0,0,0) 100%),
    radial-gradient(ellipse 260px 90px at 600px 280px,rgba(215,232,248,.85) 0%,rgba(120,175,225,.35) 55%,rgba(0,0,0,0) 100%),
    radial-gradient(ellipse 240px 160px at 220px 110px,rgba(40,110,175,.75) 0%,rgba(0,0,0,0) 100%),
    radial-gradient(ellipse 200px 120px at 200px 260px,rgba(110,165,215,.55) 0%,rgba(0,0,0,0) 100%),
    linear-gradient(100deg,#0a2140 0%,#123a66 35%,#1d5f98 65%,#2b6fa8 100%)}
.hero-caption{right:48px;top:240px;text-align:right;font-family:'Cinzel',serif;font-size:16.5px;line-height:21px;color:var(--white);letter-spacing:.6px;text-shadow:0 1px 3px rgba(0,0,0,.6)}
.hero-arrow{top:190px;width:16px;height:26px;background:rgba(255,255,255,.85);display:flex;align-items:center;justify-content:center}

/* about */
.section-title{left:0;width:727px;text-align:center;font-family:'Cinzel',serif;font-size:20.5px;font-weight:400;color:var(--ink);letter-spacing:.3px}
.section-title .accent{color:var(--blue)}
.rule{height:2px;background:var(--blue)}
.about-text{left:56px;top:424px;width:616px;text-align:center;font-size:8.4px;line-height:14px;color:var(--text)}
.btn{left:326px;top:497px;width:75px;height:22px;background:var(--blue);color:var(--white);font-size:8.5px;font-weight:700;display:flex;align-items:center;justify-content:center;box-shadow:0 2px 0 var(--blue-dark)}

/* why */
.why-photo{left:0;top:555px;width:363px;height:225px;
  background:
    radial-gradient(ellipse 70px 90px at 285px 110px,rgba(235,205,185,.55) 0%,rgba(0,0,0,0) 100%),
    radial-gradient(ellipse 120px 110px at 70px 60px,rgba(70,55,50,.8) 0%,rgba(0,0,0,0) 100%),
    radial-gradient(ellipse 140px 90px at 100px 200px,rgba(25,28,34,.9) 0%,rgba(0,0,0,0) 100%),
    radial-gradient(ellipse 130px 100px at 300px 210px,rgba(55,58,64,.85) 0%,rgba(0,0,0,0) 100%),
    radial-gradient(ellipse 80px 80px at 220px 40px,rgba(190,185,180,.7) 0%,rgba(0,0,0,0) 100%),
    linear-gradient(135deg,#e8e8e6 0%,#c9cacb 40%,#7b7f85 75%,#3e424a 100%)}
.why-panel{left:363px;top:555px;width:364px;height:225px;background:var(--blue);color:var(--white)}
.why-title{left:32px;top:20px;font-family:'Cinzel',serif;font-size:21px;font-weight:400;letter-spacing:.6px}
.why-rule{left:32px;top:54px;width:283px;height:1px;background:rgba(255,255,255,.6)}
.why-lead{left:32px;top:70px;width:300px;font-size:9.2px;line-height:14px;font-weight:700}
.why-list{left:32px;top:112px;list-style:none;font-size:8.3px}
.why-list li{display:flex;align-items:center;gap:7px;height:18.5px}

/* address check */
.check{left:0;top:780px;width:727px;height:147px;background:var(--light)}
.field{top:87px;height:26px;background:var(--white);border:1px solid #d3d3d3;font-size:8px;color:#444;padding-left:10px;display:flex;align-items:center}
.go{left:533px;top:87px;width:43px;height:26px;background:var(--blue);color:var(--white);font-size:12px;font-weight:700;display:flex;align-items:center;justify-content:center;box-shadow:0 2px 0 var(--blue-dark)}

/* partners */
.partners{left:0;top:927px;width:727px;height:109px;background:var(--band)}
.partner{top:33px;width:92px;height:43px;background:var(--white);display:flex;align-items:center;justify-content:center;gap:6px;font-size:14px;color:#222}
.partner .dot{width:14px;height:14px;border-radius:50%;border:2px solid #222}

/* footer */
.footer{left:0;top:1036px;width:727px;height:136px;background:var(--footer);color:var(--footer-text)}
.col-title{font-family:'Cinzel',serif;font-size:10.5px;color:var(--white);letter-spacing:.5px;padding-bottom:4px;border-bottom:1px solid #666}
.links{list-style:none;font-size:8px;line-height:18.3px}
.links li::before{content:"›";margin-right:5px}
.contact-line{font-size:8px;line-height:12px;display:flex;gap:7px}
.sep{top:12px;width:1px;height:110px;background:#444}
.map{left:336px;top:41px;width:148px;height:80px;border:2px solid var(--white);
  background:
    radial-gradient(ellipse 40px 25px at 75px 40px,rgba(240,200,120,.8) 0%,rgba(0,0,0,0) 100%),
    linear-gradient(135deg,#c7d9a8 0%,#e8e3d0 40%,#8fb4d9 100%)}
.foot-brand{left:527px;top:62px;display:flex;align-items:center;gap:10px}
.foot-brand .mark{width:34px;height:34px;border-radius:50%;border:3px solid #aaa}
.foot-brand .name{font-family:'Cinzel',serif;font-size:17px;line-height:19px;color:#ddd}

.bottom{left:0;top:1172px;width:727px;height:28px;background:var(--blue);color:var(--white)}
.copy{left:50px;top:9px;font-size:7.5px;font-weight:700}
.social{top:5px;width:18px;height:18px;border-radius:50%;background:#1d5d8f;border:1.5px solid var(--white)}
</style>
</head>
<body>

<header class="abs header">
  <div class="abs topline"></div>
  <div class="abs brand">
    <span class="mark"></span>
    <span class="name">Quill Harbor<br>Internet</span>
  </div>
  <div class="abs phone">
    <svg width="12" height="12" viewBox="0 0 24 24"><circle cx="12" cy="12" r="11" fill="none" stroke="#3d9ad1" stroke-width="2"/><path d="M8 6l3 3-1.5 1.5c.8 1.7 2.3 3.2 4 4L15 13l3 3-2 2c-4 0-10-6-10-10z" fill="#3d9ad1"/></svg>
    123 456 7890
  </div>
  <div class="abs mail-tab">
    <svg width="10" height="7" viewBox="0 0 10 7"><rect width="10" height="7" fill="#fff"/><path d="M0 0l5 4 5-4" stroke="#3d9ad1" fill="none"/></svg>
    info@quillharborinternet.com
  </div>
  <nav class="abs nav">
    <a>Home</a><a>Who We Are</a><a>Partners</a><a>Technologies</a><a>Contact Us</a>
  </nav>
</header>

<section class="abs hero" role="img" aria-label="Photo of network cables against glowing blue fibre optic strands">
</section>
<div class="abs hero-caption">Bringing Businesses together for<br>better more affordable Internet</div>
<div class="abs hero-arrow" style="left:0;border-radius:0 13px 13px 0">
  <svg width="8" height="10" viewBox="0 0 8 10"><path d="M6 1L2 5l4 4" stroke="#333" stroke-width="1.6" fill="none"/></svg>
</div>
<div class="abs hero-arrow" style="right:0;border-radius:13px 0 0 13px">
  <svg width="8" height="10" viewBox="0 0 8 10"><path d="M2 1l4 4-4 4" stroke="#333" stroke-width="1.6" fill="none"/></svg>
</div>

<h1 class="abs section-title" style="top:373px">About <span class="accent">Quill Harbor</span> Internet</h1>
<div class="abs rule" style="left:316px;top:408px;width:94px"></div>
<p class="abs about-text">Lorem ipsum dolor sit amet, consectetuer adipiscing elit, sed diam nonummy nibh euismod tincidunt ut laoreet dolore magna aliquam erat volutpat. Ut wisi enim ad minim veniam, quis nostrud exerci tation ullamcorper suscipit lobortis nisl ut aliquip ex ea commodo consequat. Duis autem vel eum iriure dolor in hendrerit in vulputate velit esse molestie consequat, vel illum dolore eu feugiat nulla facilisis at vero eros et accumsan et iusto odio dignissim qui blandit praesent luptatum zzril delenit augue duis dolore te feugait nulla facilisi.</p>
<div class="abs btn">READ MORE</div>

<div class="abs why-photo" role="img" aria-label="Photo of three business people working together at a laptop"></div>
<section class="abs why-panel">
  <h2 class="abs why-title">Why Choose Us?</h2>
  <div class="abs why-rule"></div>
  <p class="abs why-lead">Ut wisi enim ad minim veniam, quis nostrud exerc tationmcorper. hendrerit inmi vulputate velit it lobortis nisl ut aliquip</p>
  <ul class="abs why-list">
    <li><svg width="9" height="9" viewBox="0 0 10 10"><circle cx="5" cy="5" r="4.3" fill="none" stroke="#fff"/><path d="M2.8 5l1.6 1.6L7.4 3.4" stroke="#fff" stroke-width="1.3" fill="none"/></svg>Ut wisi enim ad minim veniam, quis nostrud exerci</li>
    <li><svg width="9" height="9" viewBox="0 0 10 10"><circle cx="5" cy="5" r="4.3" fill="none" stroke="#fff"/><path d="M2.8 5l1.6 1.6L7.4 3.4" stroke="#fff" stroke-width="1.3" fill="none"/></svg>Smod tincidunt ut laoreet dolore magna aliquam erat vol</li>
    <li><svg width="9" height="9" viewBox="0 0 10 10"><circle cx="5" cy="5" r="4.3" fill="none" stroke="#fff"/><path d="M2.8 5l1.6 1.6L7.4 3.4" stroke="#fff" stroke-width="1.3" fill="none"/></svg>To odio dignissim qui blandit praesent luptatumoil</li>
    <li><svg width="9" height="9" viewBox="0 0 10 10"><circle cx="5" cy="5" r="4.3" fill="none" stroke="#fff"/><path d="M2.8 5l1.6 1.6L7.4 3.4" stroke="#fff" stroke-width="1.3" fill="none"/></svg>Enim ad minim veniam, quis nostrud exerci laoreet dolore</li>
    <li><svg width="9" height="9" viewBox="0 0 10 10"><circle cx="5" cy="5" r="4.3" fill="none" stroke="#fff"/><path d="M2.8 5l1.6 1.6L7.4 3.4" stroke="#fff" stroke-width="1.3" fill="none"/></svg>Putate velit esse molestie consequat, vel illum dolore eu</li>
  </ul>
</section>

<section class="abs check">
  <h2 class="abs section-title" style="top:25px"><span class="accent">Check your</span> Address Now</h2>
  <div class="abs" style="left:222px;top:60px;width:283px;height:1px;background:#bcbcbc"></div>
  <div class="abs rule" style="left:316px;top:59px;width:94px"></div>
  <div class="abs field" style="left:146px;width:198px">Address</div>
  <div class="abs field" style="left:361px;width:155px">Zipcode</div>
  <div class="abs go">GO</div>
</section>

<section class="abs partners">
  <svg class="abs" style="left:28px;top:40px" width="14" height="30" viewBox="0 0 14 30"><path d="M12 1L2 15l10 14" stroke="#9a9a9a" stroke-width="1.5" fill="none"/></svg>
  <div class="abs partner" style="left:48px"><span class="dot"></span>Corvane</div>
  <div class="abs partner" style="left:155px">Maldrift</div>
  <div class="abs partner" style="left:263px">Tessor</div>
  <div class="abs partner" style="left:371px">Pylith</div>
  <div class="abs partner" style="left:478px"><span class="dot"></span>Corvane</div>
  <div class="abs partner" style="left:586px">Nimbrel</div>
  <svg class="abs" style="left:685px;top:40px" width="14" height="30" viewBox="0 0 14 30"><path d="M2 1l10 14L2 29" stroke="#b5b5b5" stroke-width="1.5" fill="none"/></svg>
</section>

<footer class="abs footer">
  <div class="abs" style="left:50px;top:14px;width:78px">
    <div class="col-title">Quick Links</div>
    <ul class="links" style="margin-top:8px">
      <li>Home</li><li>Who We Are</li><li>Partners</li><li>Technologies</li><li>Contact Us</li>
    </ul>
  </div>
  <div class="abs sep" style="left:145px"></div>
  <div class="abs" style="left:166px;top:14px;width:130px">
    <div class="col-title">Contact Details</div>
    <div class="contact-line" style="margin-top:10px">
      <svg width="8" height="10" viewBox="0 0 8 10"><path d="M4 0a3.5 3.5 0 0 1 3.5 3.5C7.5 6 4 10 4 10S.5 6 .5 3.5A3.5 3.5 0 0 1 4 0z" fill="#ccc"/><circle cx="4" cy="3.5" r="1.3" fill="#2a2a2a"/></svg>
      <span><b style="color:#fff">Quill Harbor Internet</b><br>3481 Lorem ipsum dolor amet,<br>consectetuer adipiscing , 45439</span>
    </div>
    <div class="contact-line" style="margin-top:12px">
      <svg width="8" height="9" viewBox="0 0 24 24"><path d="M5 2l5 5-2.5 2.5c1.3 2.8 3.8 5.3 6.5 6.5L16.5 14l5 5-3 3C11 22 2 13 2 5z" fill="#ccc"/></svg>
      <span>123 456 7890</span>
    </div>
    <div class="contact-line" style="margin-top:14px">
      <svg width="9" height="7" viewBox="0 0 10 7"><rect width="10" height="7" fill="#ccc"/><path d="M0 0l5 4 5-4" stroke="#2a2a2a" fill="none"/></svg>
      <span>info@quillharborinternet.com</span>
    </div>
  </div>
  <div class="abs sep" style="left:314px"></div>
  <div class="abs" style="left:338px;top:14px;width:146px">
    <div class="col-title">Location Map</div>
  </div>
  <div class="abs map" role="img" aria-label="Street map showing the office location"></div>
  <div class="abs sep" style="left:508px"></div>
  <div class="abs foot-brand">
    <span class="mark"></span>
    <span class="name">Quill Harbor<br>Internet</span>
  </div>
</footer>

<div class="abs bottom">
  <div class="abs copy">Copyright © 2016 Quill Harbor Internet. All Rights Reserved.</div>
  <span class="abs social" style="left:612px"></span>
  <span class="abs social" style="left:634px"></span>
  <span class="abs social" style="left:656px"></span>
</div>

</body>
</html>
```